Create a Magazine Ad for an asbestos law firm

we need an 8 X 13 ad to be on the back of a magazine cover. We have the text Attached and want a similar look and feel to our website : www.harborvale-claims.example. The ad should be targeted to white males 55 years or older who are conservative and worked in industry or industrial plants. The main offer is a free case review and trying to get them to call the telephone number.

Target Market(s)

White collar men who worked in industrial plants. Age 55 years or older.

Industry/Entity Type

Legal

Requirements
Must have
• Pictures of white middle class conservative man or man and woman
Nice to have
• look at www.harborvale-claims.example to an. idea of what we are looking for

```html
<!DOCTYPE html>
<html lang="en">
<head>
<meta charset="utf-8">
<title>Harborvale Claims – Mesothelioma Compensation Ad</title>
<link rel="stylesheet" href="https://fonts.googleapis.com/css2?family=Montserrat:wght@400;500;600;700&display=swap">
<style>
:root{
  --bg-top:#8aeafb;
  --bg-bottom:#6fd6f4;
  --ink:#14283a;
  --accent:#0a8ee0;
  --accent-bright:#3a4cff;
  --button:#3347ff;
  --footer:#3650ff;
  --footer-tail:#3f9cf0;
  --photo-a:#7fd5f6;
  --photo-b:#4f9ef0;
}
*{margin:0;padding:0;box-sizing:border-box}
html,body{width:721px;height:1200px;overflow:hidden}
body{font-family:"Montserrat",sans-serif;color:var(--ink);background:var(--bg-bottom)}
.ad{position:relative;width:721px;height:1200px;background:linear-gradient(180deg,var(--bg-top) 0%,var(--bg-bottom) 100%);overflow:hidden}
.abs{position:absolute}
.photo{left:0;top:790px;width:721px;height:354px;background:linear-gradient(180deg,rgba(127,213,246,0) 0%,var(--photo-a) 25%,var(--photo-b) 100%)}
.brand{left:392px;top:30px;display:flex;align-items:center;gap:8px}
.brand-dot{width:30px;height:30px;border-radius:50%;background:var(--accent);opacity:.55}
.brand-name{font-size:22px;font-weight:500;color:#2a4a60;line-height:1}
.brand-tag{left:432px;top:60px;font-size:7px;color:#2a4a60;letter-spacing:.1px}
.head-left{left:49px;top:80px;line-height:1}
.light{font-weight:400}
.strong{font-weight:700;color:var(--accent)}
.head-left .l1{font-size:29px}
.head-left .l2{font-size:36px;margin-top:2px}
.head-left .l3{font-size:29px;margin-top:14px}
.head-left .l4{font-size:29px}
.head-right{left:381px;top:122px;line-height:1}
.head-right .big{font-size:42px;font-weight:700;color:var(--accent)}
.head-right .mid{font-size:21px;margin-top:2px}
.head-right .sub{font-size:27px;font-weight:700;color:var(--accent);margin-top:6px}
.body{font-size:11.2px;line-height:14.2px}
.list{border-left:1px solid var(--ink);padding-left:6px}
.p1{left:27px;top:250px;width:320px}
.l1list{left:45px;top:299px}
.p2{left:25px;top:375px;width:260px}
.l2list{left:45px;top:413px;width:300px}
.p3{left:362px;top:260px;width:330px}
.eligible{left:24px;top:520px;font-size:15.5px;line-height:18px}
.eligible b{color:var(--accent-bright);font-weight:700}
.eligible .k{font-weight:700}
.eligible-note{left:27px;top:558px;font-size:11.2px;line-height:14px;font-weight:600;width:310px}
.cta-line{left:49px;top:622px;width:295px;text-align:center;font-size:16px}
.cta-line b{font-weight:700}
.cta-line .hl{color:var(--accent-bright);font-weight:700}
.call-bar{left:49px;top:657px;width:295px;height:26px;background:var(--button);border-top-left-radius:18px;color:#fff;font-weight:700;font-size:11px;display:flex;align-items:center;justify-content:center;letter-spacing:.3px}
.call-box{left:55px;top:697px;width:286px;height:42px;border:1px solid var(--ink);border-top-left-radius:22px;display:flex;align-items:center;justify-content:center;color:var(--accent-bright);font-size:23px;font-weight:600}
.q{left:361px;top:398px;font-size:22.5px;line-height:27px}
.q .m{color:var(--accent-bright);font-weight:700}
.q .meso{color:var(--accent-bright)}
.p4{left:361px;top:485px;width:330px}
.settle{left:373px;top:595px;border-left:1px solid var(--ink);padding-left:7px}
.settle li{list-style:none;margin-bottom:13.5px}
.settle li:last-child{margin-bottom:0}
.footer{left:0;top:1144px;width:721px;height:26px;background:var(--footer);color:#fff;font-weight:700;font-size:11px;display:flex;align-items:center;justify-content:center}
.footer-tail{left:0;top:1170px;width:721px;height:30px;background:var(--footer-tail)}
</style>
</head>
<body>
<div class="ad">
  <div class="abs photo" role="img" aria-label="Photo of an older man and woman sitting on a sofa, talking, tinted blue"></div>

  <div class="abs brand"><span class="brand-dot"></span><span class="brand-name">Harborvale Claims</span></div>
  <div class="abs brand-tag">Over 20 years of fighting for mesothelioma patients and families</div>

  <div class="abs head-left">
    <div class="l1 light">Diagnosed with</div>
    <div class="l2 strong">Mesothelioma,</div>
    <div class="l3 light">You could be Owed</div>
    <div class="l4 strong">Compensation</div>
  </div>

  <div class="abs head-right">
    <div class="big">$30 Billion</div>
    <div class="mid light">is Available in Trust for</div>
    <div class="sub">Mesothelioma Patients</div>
  </div>

  <p class="abs body p1">It's very likely you developed this disease through asbestos exposure. Mesothelioma patients are getting multi-million dollar settlements, decades later, fromt</p>
  <div class="abs body list l1list">Exposure to asbestos products,<br>Ex-employers, or<br>Talcum baby powder companies</div>

  <p class="abs body p2">We can help you find out if you qualify for a case in minutes</p>
  <div class="abs body list l2list">We'll analyze your situation at no cost,<br>Determine how much compensation you could be entitled too,<br>Show you the next steps to get what you're owed.</div>

  <p class="abs body p3">Tradesmen in many industries were negligently exposed to asbestos materials well into the 1990s. Whether you developed Mesothelioma yourself due to asbestos exposure or you're the surviving family of a lost loved one youcould be entitled to significant compensation</p>

  <div class="abs eligible"><b>Find out</b> if you're <b>Eligible,</b><br>for <b>FREE</b><span class="k">, in</span> <b>Minutes</b></div>
  <p class="abs eligible-note">We'll evaluate your situation and tell you what your case could be worth</p>

  <div class="abs cta-line">Get your <b>Free</b> <span class="hl">evaluation</span> <b>now!</b></div>
  <div class="abs call-bar">CALL 1-XXX XXXX</div>
  <div class="abs call-box">Call now</div>

  <h2 class="abs q light">How much <span class="m">Money</span> Can<br>People Receive from a<br><span class="meso">Mesothelioma</span> Case?</h2>
  <p class="abs body p4">Depending on where you were exposed and a few other factors, you can get a settlement from 6 to 7 figures. Here are a few examples of Mesothelioma Settlements received by our clients. These figures are the total compensation after all attorney fees and expenses are deducted.</p>

  <ul class="abs body settle">
    <li>$6,142,500<br>Exposed through heavy duty vehicles</li>
    <li>$6,033,510<br>Exposed through general contracting</li>
    <li>$5,939,010<br>Exposed through boat repair</li>
    <li>$3,921,750<br>Exposed through navy service</li>
    <li>$3,600,450<br>Exposed through navy service</li>
    <li>$2.5 Million<br>Exposed from Brightwell Talcum Baby Powder.</li>
  </ul>

  <div class="abs footer">Marlow &amp; Keene, LLP, Daniel Marlow, Galveston, TX</div>
  <div class="abs footer-tail"></div>
</div>
</body>
</html>
```